Fresh easy to read restaurant menu

Burger Restaurant menu based on an island in Thailand. Light colours because we have dimmed lights and it needs to be easy to read. Need to fit on A3 size paper/ 2 sides. COULD BE LANDSCAPE POSITION TOO.
Colour choices around existing logo. Vintage fun look if possible. Owner needs to be able to change text when menu needs to change.
Have different major sections (Starters - Juicy burgers and sandwiches - Crunchy salads - Tasty meals - Sweet bites & desserts) smaller sections (Extras - Dips, mayos and more - Zindle's special thirst quenchers)
I uploaded my last menu design. I need a fresh look as we have used this last one for the past 4 years.
Please make sure it's not too dark and easy to read. LANDSCAPE is better. The menu items needs to the editable because we are located on a thai island and products are not always available. Prices needs constant changes too as we have low and high seasons.
Thanks for your time and effort.
Reason: Still looking for the right design. Some designers have committed but not enough time to submit designs.
Restaurant

```html
<!DOCTYPE html>
<html lang="en">
<head>
<meta charset="utf-8">
<title>Zindle's Restaurant &amp; Lounge Menu</title>
<link rel="stylesheet" href="https://fonts.googleapis.com/css2?family=Bubblegum+Sans&family=Courgette&family=Open+Sans:wght@600;700&display=swap">
<style>
:root{
  --sand:#f9e3a0;
  --sand-light:#fbecb8;
  --peach:#f5a47c;
  --peach-light:#f8b590;
  --ink:#1f1a17;
  --orange-head:#ee7a35;
  --blue-head:#3aa9e2;
  --box-peach:#f39a6b;
  --box-sand:#f8dc8f;
  --leaf:#5f9a3c;
  --leaf-light:#8cc05a;
  --wood:#b57a3e;
  --white:#ffffff;
}
*{box-sizing:border-box;margin:0;padding:0}
html,body{width:1200px;height:849px;overflow:hidden;background:var(--white)}
.menu{position:relative;width:1200px;height:849px;overflow:hidden;font-family:"Open Sans",Arial,sans-serif;color:var(--ink)}
.panel{position:absolute;top:0;height:849px}
.panel-left{left:0;width:602px;background:radial-gradient(circle at 40% 40%,var(--sand-light),var(--sand))}
.panel-right{left:602px;width:598px;background:radial-gradient(circle at 50% 45%,var(--peach-light),var(--peach))}
.foliage{position:absolute;background:radial-gradient(ellipse at 50% 20%,var(--leaf-light),var(--leaf));opacity:.8}
.foliage-left{left:0;top:0;width:375px;height:105px;border-radius:0 0 55% 45%}
.foliage-right{right:0;top:0;width:317px;height:115px;border-radius:0 0 15% 85%}
.brand{position:absolute;left:440px;top:30px;width:290px;height:80px;display:flex;align-items:center;justify-content:center;gap:10px}
.brand-dot{width:20px;height:20px;border-radius:50%;background:var(--wood)}
.brand-name{font-family:"Bubblegum Sans",cursive;font-size:48px;line-height:1;color:var(--wood)}
.section-title{position:absolute;font-family:"Bubblegum Sans",cursive;font-weight:400;text-align:center;letter-spacing:1px;line-height:1.2;
  -webkit-text-stroke:1.5px var(--white);paint-order:stroke fill;text-shadow:0 0 3px var(--white)}
.title-orange{color:var(--orange-head)}
.title-blue{color:var(--blue-head)}
.title-xl{font-size:30px}
.title-md{font-size:21px}
.title-sm{font-size:18px}
.item{position:absolute;display:flex;justify-content:space-between;align-items:baseline;white-space:nowrap}
.item-left{left:34px;width:533px}
.item-right{left:632px;width:534px}
.item-name{font-weight:700;font-size:15px}
.desc{font-family:"Courgette",cursive;font-weight:400;font-size:11px}
.price{font-weight:700;font-size:15px}
.note{position:absolute;font-family:"Courgette",cursive;font-size:11px;line-height:15px}
.note-left{left:34px}
.center-note{position:absolute;text-align:center;font-family:"Courgette",cursive;font-size:11.5px;line-height:16px}
.size-prices{position:absolute;left:42px;width:513px;text-align:center;font-weight:700;font-size:15px}
.extras-box{position:absolute;border:2px solid var(--white);border-radius:8px;font-family:"Courgette",cursive;font-size:12px}
.box-sauces{left:40px;top:746px;width:515px;height:89px;background:var(--box-peach);padding:7px 14px;display:grid;grid-template-columns:1.1fr 1.3fr 1fr;line-height:18px}
.box-toppings{left:639px;top:744px;width:519px;height:91px;background:var(--box-sand);padding:9px 26px;display:grid;grid-template-columns:1fr 1fr;column-gap:30px}
.topping{display:flex;justify-content:space-between;line-height:18px}
.topping small{font-size:9px}
</style>
</head>
<body>
<main class="menu">
  <section class="panel panel-left"></section>
  <section class="panel panel-right"></section>
  <div class="foliage foliage-left" role="img" aria-label="Palm leaves"></div>
  <div class="foliage foliage-right" role="img" aria-label="Palm leaves"></div>

  <div class="brand"><span class="brand-dot"></span><span class="brand-name">Zindle's</span></div>

  <!-- Starters -->
  <h2 class="section-title title-orange title-xl" style="left:0;width:602px;top:126px">HUNGER MANAGEMENT</h2>
  <div class="item item-left" style="top:164px"><span class="item-name">Homemade Fries</span><span class="price">70</span></div>
  <div class="item item-left" style="top:196px"><span class="item-name">Battered Onion bunch with dip</span><span class="price">100</span></div>
  <div class="item item-left" style="top:227px"><span class="item-name">Indian Roasted Chickpeas <span class="desc">- A low fat and nutritious beer snack!</span></span><span class="price">60</span></div>
  <div class="item item-left" style="top:258px"><span class="item-name">Crispy Raviolis <span class="desc">- Served with Marinara Sauce</span></span><span class="price">90</span></div>
  <div class="item item-left" style="top:290px"><span class="item-name">Yummy Hummus <span class="desc">- Served with Cracker &amp; Veggies</span></span><span class="price">120</span></div>
  <div class="item item-left" style="top:321px"><span class="item-name">Hummus Plate <span class="desc">- Meal size portion with a choice of one topping:</span></span><span class="price">180</span></div>
  <p class="note note-left" style="top:343px">Feta, chicken, bacon, olives, jalapenos, mushrooms, fried onions or<br>roasted chickpeas. Served with crackers &amp; veggies</p>
  <div class="item item-left" style="top:392px"><span class="item-name">Smoked Salmon Starter <span class="desc">- Served on cucumber slices with dill cream cheese</span></span><span class="price">140</span></div>
  <div class="item item-left" style="top:422px"><span class="item-name">Chicken Wings <span class="desc">(Regular or Super Spicy)</span></span><span class="price">130</span></div>
  <p class="note note-left" style="top:444px">Extra Blue Cheese Dip ................ 30</p>
  <div class="item item-left" style="top:471px"><span class="item-name">Garlic Bread</span><span class="price">80</span></div>
  <p class="note note-left" style="top:493px">Extra Cheese ................ 40</p>
  <div class="item item-left" style="top:523px"><span class="item-name">Warm Cheese Dip <span class="desc">- Served with baked tortilla chips</span></span><span class="price">150</span></div>
  <div class="item item-left" style="top:555px"><span class="item-name">Poutine <span class="desc">- French fries, gravy &amp; cheese...</span></span><span class="price">130</span></div>
  <p class="note note-left" style="top:576px">The most popular munchies from Québec, Canada!<br>Extra minced beef ................ 60<br>Extra pulled pork, chicken or bacon ................ 50<br>Mexican Style ................ 50 (jalapenos, onions, tomatoes and sour cream)</p>

  <!-- Dips -->
  <h3 class="section-title title-orange title-sm" style="left:42px;width:513px;top:670px">MAYO, DIPS &amp; MORE</h3>
  <p class="center-note" style="left:42px;width:513px;top:696px">Pimp up your Fries and Burgers with our tasty Homemade Sauces</p>
  <p class="size-prices" style="top:719px">SINGLE - 30 | DUO - 50 | TRIO - 70</p>
  <div class="extras-box box-sauces">
    <span>Chili Mayo</span><span>Sweet BBQ Sauce</span><span>Gravy</span>
    <span>Garlic Mayo</span><span>Blue Cheese Dip</span><span>Marinara Sauce</span>
    <span>Ranch Mayo</span><span>Thousand Island Dressing</span><span>Sour Cream</span>
    <span>Honey Mustard Mayo</span><span>Hummus</span><span>Olive Tapenade</span>
  </div>

  <!-- Burgers -->
  <h2 class="section-title title-blue title-xl" style="left:602px;width:598px;top:126px">FAMOUS SEXY BURGERS</h2>
  <p class="center-note" style="left:602px;width:598px;top:168px">Available with first quality BEEF, grilled CHICKEN breast or homemade VEGGIE patty.<br>Served with fries and coleslaw.&nbsp; Get a POUTINE side instead for an extra 50b.</p>
  <div class="item item-right" style="top:209px"><span class="item-name">The Classic</span><span class="price">170</span></div>
  <div class="item item-right" style="top:240px"><span class="item-name">The Cheesy Cheddar</span><span class="price">190</span></div>
  <div class="item item-right" style="top:271px"><span class="item-name">The Hotty <span class="desc">- With chilli mayo and jalapenos... HOT!</span></span><span class="price">190</span></div>
  <div class="item item-right" style="top:302px"><span class="item-name">The Vics <span class="desc">- With blue cheese, fried onions &amp; mushrooms</span></span><span class="price">200</span></div>
  <div class="item item-right" style="top:334px"><span class="item-name">The Med <span class="desc">- With feta, slow-roasted tomatoes, olive tapenade &amp; hummus</span></span><span class="price">200</span></div>
  <div class="item item-right" style="top:365px"><span class="item-name">The Delux <span class="desc">- With bacon, homemade mayonnaise &amp; brie cheese</span></span><span class="price">210</span></div>
  <div class="item item-right" style="top:396px"><span class="item-name">The ZINDLE <span class="desc">- With onion rings, bacon, sweet BBQ sauce &amp; thousand island dressing</span></span><span class="price">220</span></div>
  <div class="item item-right" style="top:428px"><span class="item-name">The Pizza <span class="desc">- Pepperoni, mozzarella, pizza sauce &amp; mushrooms</span></span><span class="price">220</span></div>
  <div class="item item-right" style="top:459px"><span class="item-name">The Animal <span class="desc">- Two beef patties, BBQ sauce, pickles, coleslaw, egg &amp; crispy onions</span></span><span class="price">250</span></div>
  <div class="item item-right" style="top:490px"><span class="item-name">The Fat Betty <span class="desc">- DOUBLE BEEF patty with melting cheese middle</span></span><span class="price">250</span></div>

  <!-- Sandwiches -->
  <h3 class="section-title title-blue title-md" style="left:602px;width:598px;top:530px">TOASTED SANDWICHES</h3>
  <div class="item item-right" style="top:565px"><span class="item-name">Jalapeno Grilled Cheese <span class="desc">- Cream cheese, cheddar, marinara sauce &amp; green onion.</span></span><span class="price">170</span></div>
  <p class="note" style="left:632px;top:587px">Extra bacon ................ 40</p>
  <div class="item item-right" style="top:615px"><span class="item-name">Pulled Pork Sandwich <span class="desc">- Slow-roasted pork &amp; mozzarella sandwich toasted on the grill</span></span><span class="price">190</span></div>
  <div class="item item-right" style="top:646px"><span class="item-name">Patty Melt <span class="desc">- With thin beef patty, fried onions, cheddar &amp; thousand island dressing</span></span><span class="price">190</span></div>

  <!-- Burger extras -->
  <h3 class="section-title title-blue title-sm" style="left:602px;width:598px;top:712px">Make your Burger EXTRA Special With</h3>
  <div class="extras-box box-toppings">
    <div>
      <div class="topping"><span>Fried Onions or Mushrooms</span><span>30</span></div>
      <div class="topping"><span>Cheese <small>(Cheddar, Feta, Brie,</small></span><span>40</span></div>
      <div class="topping"><span><small>Blue, Mozz or Cream Cheese)</small></span><span></span></div>
      <div class="topping"><span>Bacon or Pepperoni</span><span>40</span></div>
    </div>
    <div>
      <div class="topping"><span>Pickles or Jalapenos</span><span>20</span></div>
      <div class="topping"><span>Fried Egg</span><span>20</span></div>
      <div class="topping"><span>Smoked Salmon</span><span>60</span></div>
    </div>
  </div>
</main>
</body>
</html>
```